New Company Business Card Design

I have a new company logo and I want a new business card design. I dont know if the logo file i attached is in the correct format or quality. We are a New York City Specialty construction Firm specializing in high risk out of the box projects. I want a simple and classy business card that people will his card is as crisp as the work his company does.

Target Market(s)

Clients in the heavy construction industry in New York City

Industry/Entity Type

Construction Company

Contact Information for Business Card

Simple Classy - DIFFERENT

Font styles to use
Other font styles liked:
• Mach the logo font in some way

Colors

Designer to choose colors to be used in the design.

Requirements
Must have
• Uniqueness
Nice to have
• Nothing particular - Just different and classy - Timeless
Should not have
• Goofy Shit or Gimmicky shit

```html
<!DOCTYPE html>
<html lang="en">
<head>
<meta charset="utf-8">
<title>KRT Associates, Inc — Business Card</title>
<link rel="stylesheet" href="https://fonts.googleapis.com/css2?family=Cinzel:wght@700&family=Tenor+Sans&display=swap">
<style>
  :root {
    --page: #ffffff;
    --card-edge: #111111;
    --white: #ffffff;
    --pink: #c4659a;
    --blue: #2a6db5;
    --navy: #1d1a5e;
    --black: #000000;
    --grey-band: #666666;
    --grey-name: #242424;
    --serif: "Cinzel", "Trajan Pro", serif;
    --sans: "Tenor Sans", "Optima", sans-serif;
  }
  html, body {
    margin: 0;
    width: 1200px;
    height: 1200px;
    overflow: hidden;
    background: var(--page);
  }
  .sheet { position: relative; width: 1200px; height: 1200px; }
  .card {
    position: absolute;
    width: 968px;
    height: 532px;
    border: 2px solid var(--card-edge);
    border-radius: 3px;
    overflow: hidden;
    box-sizing: border-box;
  }
  .card--colour { left: 115px; top: 28px; }
  .card--mono { left: 115px; top: 643px; }
  .card svg { display: block; width: 100%; height: 100%; }

  .brand-name { font-family: var(--serif); font-weight: 700; font-size: 128px; letter-spacing: 40px; }
  .brand-corner { font-family: var(--serif); font-weight: 700; font-size: 34px; letter-spacing: 12px; }
  .company-line { font-family: var(--sans); font-size: 50px; fill: var(--white); }
  .company-line .suffix { font-size: 36px; }

  .card--colour .accent { fill: var(--pink); }
  .card--colour .band { fill: var(--blue); }
  .card--colour .ink { fill: var(--navy); }

  .card--mono .accent { fill: var(--black); }
  .card--mono .band { fill: var(--grey-band); }
  .card--mono .ink { fill: var(--grey-name); }

  .field { fill: var(--white); }
</style>
</head>
<body>
<main class="sheet">

  <section class="card card--colour" aria-label="Business card, colour version">
    <svg viewBox="0 0 964 528" preserveAspectRatio="none">
      <rect class="accent" x="0" y="0" width="964" height="528"/>
      <path class="field" d="M0,48 C330,2 760,40 964,150 L964,396 C820,470 660,505 420,512 L0,512 Z"/>
      <path class="band" d="M0,432 C210,400 470,420 612,500 C430,518 180,518 0,515 Z"/>
      <rect class="ink" x="222" y="256" width="32" height="32"/>
      <text class="brand-name ink" x="490" y="324" text-anchor="middle">KRT</text>
      <text class="brand-corner ink" x="906" y="64" text-anchor="end">KRT</text>
      <text class="company-line" x="45" y="498">ASSOCIATES,<tspan class="suffix">INC</tspan></text>
    </svg>
  </section>

  <section class="card card--mono" aria-label="Business card, greyscale version">
    <svg viewBox="0 0 964 528" preserveAspectRatio="none">
      <rect class="accent" x="0" y="0" width="964" height="528"/>
      <path class="field" d="M0,48 C330,2 760,40 964,150 L964,396 C820,470 660,505 420,512 L0,512 Z"/>
      <path class="band" d="M0,432 C210,400 470,420 612,500 C430,518 180,518 0,515 Z"/>
      <rect class="ink" x="222" y="256" width="32" height="32"/>
      <text class="brand-name ink" x="490" y="324" text-anchor="middle">KRT</text>
      <text class="brand-corner" x="906" y="64" text-anchor="end" fill="#ffffff">KRT</text>
      <text class="company-line" x="45" y="498">ASSOCIATES,<tspan class="suffix">INC</tspan></text>
    </svg>
  </section>

</main>
</body>
</html>
```